Floor Inspections and Consulting

We provide inspections and consulting services on various floor coverings, e.g. carpet, hardwood, etc. We also do expert witness work for attorneys due to floor covering failures. We current have a logo, just need it incorporated into a new design. I have examples of cards I have found on the internet that capture my attention and make a statement. I have included our original business card, which in my opinion is terrible, but it does have our logo on it.

```html
<!DOCTYPE html>
<html lang="en">
<head>
<meta charset="utf-8">
<title>Ridgeline Flooring Inspections – Business Card</title>
<link rel="stylesheet" href="https://fonts.googleapis.com/css2?family=Archivo:wght@400;800;900&display=swap">
<style>
  :root {
    --backdrop: #d9d9d9;
    --card: #1b1b1c;
    --card-edge: #232325;
    --orange: #ec7211;
    --white: #ffffff;
    --grey: #b9b9b9;
  }
  * { box-sizing: border-box; margin: 0; padding: 0; }
  html, body { width: 1200px; height: 900px; overflow: hidden; }
  body {
    background: var(--backdrop);
    font-family: "Archivo", Arial, sans-serif;
    position: relative;
  }
  .card {
    position: absolute;
    width: 525px;
    height: 300px;
    border-radius: 22px;
    background: linear-gradient(135deg, var(--card-edge) 0%, var(--card) 55%);
    box-shadow: 0 10px 24px rgba(0,0,0,0.25);
    overflow: hidden;
  }
  .card-front { left: 90px; top: 140px; }
  .card-back { left: 585px; top: 470px; }

  .mark-square { width: 26px; height: 26px; background: var(--orange); flex: none; }

  /* Front */
  .front-mark {
    position: absolute;
    left: 130px; top: 88px;
    display: flex; align-items: center; gap: 12px;
  }
  .brand-word {
    font-weight: 900; font-size: 44px; color: var(--orange);
    letter-spacing: 0.5px; line-height: 1;
  }
  .front-tagline {
    position: absolute; left: 130px; top: 160px;
    color: var(--grey); font-weight: 800; font-size: 19px; line-height: 1.2;
  }

  /* Back */
  .back-brand {
    position: absolute; left: 34px; top: 52px;
    display: flex; align-items: center; gap: 12px;
  }
  .back-brand .mark-square { width: 20px; height: 20px; }
  .brand-name {
    color: var(--orange); font-weight: 900; font-size: 22px; line-height: 1;
  }
  .person-name {
    position: absolute; left: 34px; top: 172px;
    color: var(--orange); font-weight: 900; font-size: 22px; letter-spacing: 0.5px;
    line-height: 1.2;
  }
  .website {
    position: absolute; right: 30px; top: 176px;
    color: var(--white); font-size: 16px; line-height: 1.2;
  }
  .website .accent { color: var(--orange); }
  .contact-list { position: absolute; left: 34px; top: 212px; list-style: none; }
  .contact-list li {
    display: flex; align-items: center; gap: 10px;
    color: var(--white); font-size: 16px; line-height: 1.55;
  }
  .contact-list svg { width: 16px; height: 16px; flex: none; }
</style>
</head>
<body>
  <section class="card card-front" aria-label="Card front">
    <div class="front-mark">
      <span class="mark-square"></span>
      <span class="brand-word">Ridgeline</span>
    </div>
    <p class="front-tagline">Certified Floor Covering<br>Inspection &amp; Consulting</p>
  </section>

  <section class="card card-back" aria-label="Card back">
    <div class="back-brand">
      <span class="mark-square"></span>
      <span class="brand-name">Ridgeline Flooring Inspections</span>
    </div>

    <h1 class="person-name">DANA MARLOWE</h1>
    <p class="website">www.<span class="accent">ridgelineflooring</span>.com</p>

    <ul class="contact-list">
      <li>
        <svg viewBox="0 0 16 16" aria-hidden="true">
          <rect x="1" y="1" width="14" height="14" rx="2" fill="none" stroke="var(--orange)" stroke-width="1.6"/>
          <path d="M5 4.5c-.6.5-.8 1.6 0 3.1.9 1.7 2.2 3 3.8 3.7 1.1.5 1.9.2 2.3-.4l-1.4-1.3-1 .6c-.8-.4-1.6-1.2-2-2l.6-1L6 4.3z" fill="var(--orange)"/>
        </svg>
        303-555-0148
      </li>
      <li>
        <svg viewBox="0 0 16 16" aria-hidden="true">
          <rect x="1" y="3" width="14" height="10" fill="var(--orange)"/>
          <path d="M1 3l7 6 7-6" fill="none" stroke="var(--card)" stroke-width="1.3"/>
        </svg>
        dana@ridgelineflooring.com
      </li>
    </ul>
  </section>
</body>
</html>
```